Voterra Reserve new label design.

Voterra needs a new image that communicates quality, authenticity and modernity.
Our marketing strategy is based on competitive price and good quality.

We need the design shown below (8 wines):

1. Spanish red wine
2. Spanish red wine
3. French red wine .
4. Chilean red wine .
5. Argentine red wine .
6. Mexican red wine .
7. French red wine.
8. Italian red wine .

One base design with 8 variations and colors ... we what the Cafloria line of wine per say. Or another good example is the Brisca Fizz line.
Updates

Justo to clarify an important issue: we need a new LABEL not a new logo. You can find the logo file (voterra logo 2013-grid) on the proyect. Thanks!

Target Market(s)

Premium shoppers from wine want quality and design.

Industry/Entity Type

Marketing

Requirements
Must have
• The new logo *Find it on the files. *
Year of production.
Type of grape.
Country.
Region.
Bottles preferably with the traditional silhouette of 750 ml.
Label size it´s up to you.
Nice to have
• I uploaded some examples of "line products" , this is what we are looking for to have in Voterra Reserve.

```html
<!DOCTYPE html>
<html lang="en">
<head>
<meta charset="utf-8">
<title>Voterra Reserve – Merlot label</title>
<link rel="stylesheet" href="https://fonts.googleapis.com/css2?family=Playfair+Display:ital,wght@0,400;0,700;1,400&family=Raleway:ital,wght@0,200;0,300;1,200;1,300&display=swap">
<style>
  :root {
    --backdrop: #f5f0e6;
    --label-red: #c42636;
    --dot-red: #e2323c;
    --ink-light: #f6e4e4;
    --rule: rgba(246, 228, 228, 0.55);
  }
  * { margin: 0; padding: 0; box-sizing: border-box; }
  html, body {
    width: 960px;
    height: 1200px;
    overflow: hidden;
    background: var(--backdrop);
  }
  .canvas {
    position: relative;
    width: 960px;
    height: 1200px;
    background: var(--backdrop);
  }
  .label {
    position: absolute;
    left: 247px;
    top: 100px;
    width: 466px;
    height: 1000px;
    background: var(--label-red);
    color: var(--ink-light);
    overflow: hidden;
  }
  .label__pattern {
    position: absolute;
    left: 150px;
    top: 0;
    width: 316px;
    height: 407px;
    background: radial-gradient(ellipse at 55% 45%, var(--dot-red) 0%, rgba(226, 50, 60, 0.55) 60%, rgba(226, 50, 60, 0) 100%);
  }
  .label__brand {
    position: absolute;
    left: 14px;
    top: 517px;
    transform: rotate(-90deg);
    transform-origin: left top;
    white-space: nowrap;
    font-size: 44px;
    line-height: 1;
  }
  .brand__name {
    font-family: "Playfair Display", serif;
    font-weight: 700;
  }
  .brand__line {
    font-family: "Raleway", sans-serif;
    font-weight: 200;
    margin-left: 6px;
  }
  .rule {
    position: absolute;
    left: 13px;
    width: 429px;
    height: 1.5px;
    background: var(--rule);
  }
  .rule--upper { top: 557px; }
  .rule--lower { top: 825px; }
  .label__grape {
    position: absolute;
    left: 13px;
    top: 598px;
    font-family: "Playfair Display", serif;
    font-weight: 400;
    font-size: 44px;
    line-height: 1;
  }
  .label__tick {
    position: absolute;
    left: 16px;
    top: 666px;
    width: 2px;
    height: 8px;
    background: var(--ink-light);
  }
  .label__origin {
    position: absolute;
    left: 13px;
    top: 695px;
    font-family: "Raleway", sans-serif;
    font-weight: 300;
    font-size: 33px;
    line-height: 52px;
  }
  .origin__region { font-style: italic; }
  .label__vintage {
    position: absolute;
    left: 13px;
    top: 852px;
    font-family: "Playfair Display", serif;
    font-size: 28px;
    line-height: 1;
    padding-bottom: 6px;
    border-bottom: 2px solid var(--ink-light);
  }
</style>
</head>
<body>
<main class="canvas">
  <section class="label">
    <div class="label__pattern" role="img" aria-label="Pattern of bright red grape-like dots"></div>
    <h1 class="label__brand"><span class="brand__name">Voterra</span><span class="brand__line">Reserve</span></h1>
    <div class="rule rule--upper"></div>
    <p class="label__grape">Merlot</p>
    <div class="label__tick"></div>
    <p class="label__origin"><span class="origin__country">Spain</span><br><span class="origin__region">Bordeaux</span></p>
    <div class="rule rule--lower"></div>
    <p class="label__vintage">2011</p>
  </section>
</main>
</body>
</html>
```